Business Card Design Project

I am looking for a minimal matte background/shiny (spot UV) ink monochromatic design with a splash of neon color.

the card should be 2 sided, logo only on one side - all info and possibly logo on the other.

My creative director described the colors he imagined for the design to be:
'it's a dark field, like charcoal or a really dark burgundy, or deep blue, shot through with a neon—but just a tiny bit of it. so a charcoal field with a laser-thin streak of electric lime, safety orange, or cobalt blue. really beautiful stuff.'

here are some samples of the types of cards I am trying to create:
http://www.pictavault.example/photos/dawnpress/6967376935/in/photostream -> Vandrelle Lustre

http://www.pictavault.example/photos/dawnpress/6497659409/in/photostream -> Standard Coated (14pt/matte) with SPOT UV

http://www.pictavault.example/photos/dawnpress/6497658995/in/photostream/ -> Heavy Corvane with Raised Ink

http://www.pictavault.example/photos/dawnpress/6275629165/in/photostream/ -> Standard Coated (14pt/matte) with SPOT UV

Here is my logo:
https://www.filecrate.example/s/sigym192mlh58ge/quillorb%20logotype%20final.ai

Here are the details for info:
Dorian Elwood Marsh
email - dorian@quillorb.example
mobile - 555 013 2867
web -
quillorb.example: inventive technology applications
quillorb-tv.example: innovative video advertising

please let me know if there is anything at all that you need.

Target Market(s)

mid to large agencies that require interactive design and entrepreneurial/startup individuals/companies that need application development.

Industry/Entity Type

Safety

Requirements
Must have
• logo only on one side

```html
<!DOCTYPE html>
<html lang="en">
<head>
<meta charset="utf-8">
<title>Quillorb Business Card</title>
<link rel="stylesheet" href="https://fonts.googleapis.com/css2?family=Montserrat:wght@400;500;600&display=swap">
<style>
  :root {
    --backdrop: #141b33;
    --card-top: #1f2b5e;
    --card-bottom: #141c42;
    --lime: #c6ef1f;
    --ink-white: #eef1f8;
    --ink-soft: #c9cfe0;
  }
  * { margin: 0; padding: 0; box-sizing: border-box; }
  html, body {
    width: 1200px;
    height: 900px;
    overflow: hidden;
    background: var(--backdrop);
    font-family: "Montserrat", Arial, sans-serif;
  }
  .stage {
    width: 1200px;
    height: 900px;
    display: flex;
    align-items: center;
    justify-content: center;
    gap: 40px;
  }
  .card {
    position: relative;
    width: 540px;
    height: 309px;
    border-radius: 4px;
    background: linear-gradient(160deg, var(--card-top), var(--card-bottom));
    box-shadow: 0 18px 40px rgba(0, 0, 0, 0.45);
    overflow: hidden;
  }
  .wordmark {
    display: flex;
    align-items: center;
    gap: 12px;
    font-weight: 600;
    text-transform: uppercase;
    letter-spacing: 0.28em;
    line-height: 1;
  }
  .wordmark-dot {
    width: 14px;
    height: 14px;
    border-radius: 50%;
    background: var(--lime);
  }
  .card-front .wordmark {
    position: absolute;
    left: 50%;
    top: 50%;
    transform: translate(-50%, -50%);
    font-size: 36px;
    color: var(--lime);
  }
  .card-back .wordmark {
    position: absolute;
    left: 44px;
    top: 48px;
    font-size: 28px;
    color: var(--ink-white);
  }
  .contact {
    position: absolute;
    right: 40px;
    bottom: 34px;
    width: 290px;
    font-size: 12.5px;
    line-height: 1.35;
    color: var(--ink-soft);
  }
  .contact-name {
    font-size: 17px;
    font-weight: 600;
    color: var(--lime);
    margin-bottom: 8px;
    padding-left: 56px;
  }
  .contact-row {
    display: flex;
    gap: 10px;
  }
  .contact-label {
    width: 46px;
    color: var(--lime);
  }
  .contact-list { margin-bottom: 10px; }
  .site-url {
    font-weight: 600;
    color: var(--lime);
  }
  .site-desc { color: var(--ink-white); }
</style>
</head>
<body>
  <main class="stage">
    <section class="card card-front" aria-label="Card front">
      <div class="wordmark">Quillorb<span class="wordmark-dot"></span></div>
    </section>

    <section class="card card-back" aria-label="Card back">
      <div class="wordmark">Quillorb<span class="wordmark-dot"></span></div>
      <div class="contact">
        <p class="contact-name">Dorian Elwood Marsh</p>
        <div class="contact-list">
          <div class="contact-row"><span class="contact-label">email</span><span>dorian@quillorb.example</span></div>
          <div class="contact-row"><span class="contact-label">mobile</span><span>555 013 2867</span></div>
        </div>
        <p class="site-url">quillorb.example</p>
        <p class="site-desc">inventive technology applications</p>
        <p class="site-url">quillorb-tv.example</p>
        <p class="site-desc">innovative video advertising</p>
      </div>
    </section>
  </main>
</body>
</html>
```